Business Podcaster needs a sexy book cover design for upcoming book launch

I'm launching a book called Find Your Mentor: how to accelerate your growth through reaching out, getting a response from, and leaving an impression on the people you admire most. It would be cool to have maybe a band of heroes or a single hero or something on the cover, then I'll need the spine designed, as well as the back cover which would be mostly just quotes about the book from other prominent people.

I dont want to extend it. I want to shorten it. Can I do that?

```html
<!DOCTYPE html>
<html lang="en">
<head>
<meta charset="utf-8">
<title>Find Your Mentor – Book Cover</title>
<link rel="stylesheet" href="https://fonts.googleapis.com/css2?family=Bebas+Neue&family=Crimson+Text&family=Montserrat:wght@400&display=swap">
<style>
  :root {
    --page-bg: #f2f2f2;
    --cover-top: #eaefc4;
    --cover-bottom: #e0e6b6;
    --title-blue-top: #0b6a8c;
    --title-blue-bottom: #062a5e;
    --title-black: #0a0a0a;
    --title-red-top: #7a0006;
    --title-red-bottom: #ea1e2a;
    --text-dark: #1a1a1a;
    --art-red: #d9283a;
    --art-orange: #e3a03a;
    --art-teal: #1ebccb;
    --art-green: #a8c41a;
  }
  * { margin: 0; padding: 0; box-sizing: border-box; }
  html, body {
    width: 1200px;
    height: 800px;
    overflow: hidden;
    background: var(--page-bg);
  }
  .book-cover {
    position: absolute;
    left: 372px;
    top: 40px;
    width: 456px;
    height: 720px;
    background: linear-gradient(135deg, var(--cover-top), var(--cover-bottom));
    overflow: hidden;
  }
  .title {
    position: absolute;
    font-family: "Bebas Neue", "Oswald", sans-serif;
    font-weight: 400;
    line-height: 1;
    letter-spacing: 0.01em;
    -webkit-background-clip: text;
    background-clip: text;
  }
  .title-find {
    left: 40px;
    top: 28px;
    font-size: 138px;
    color: transparent;
    background-image: linear-gradient(180deg, var(--title-blue-top), var(--title-blue-bottom));
  }
  .title-your {
    left: 232px;
    top: 68px;
    font-size: 88px;
    color: var(--title-black);
  }
  .title-mentor {
    left: 40px;
    top: 140px;
    font-size: 150px;
    color: transparent;
    background-image: linear-gradient(180deg, var(--title-red-top), var(--title-red-bottom));
  }
  .hero-illustration {
    position: absolute;
    left: 24px;
    top: 290px;
    width: 420px;
    height: 380px;
  }
  .subtitle {
    position: absolute;
    left: 192px;
    top: 286px;
    width: 230px;
    font-family: "Crimson Text", "Times New Roman", serif;
    font-size: 12.5px;
    line-height: 1.3;
    text-transform: uppercase;
    text-align: center;
    color: var(--text-dark);
  }
  .author-name {
    position: absolute;
    left: 0;
    right: 0;
    bottom: 8px;
    text-align: center;
    font-family: "Montserrat", "Helvetica", sans-serif;
    font-size: 34px;
    letter-spacing: 0.2em;
    color: var(--text-dark);
  }
</style>
</head>
<body>
  <main class="book-cover">
    <h1 class="book-title">
      <span class="title title-find">Find</span>
      <span class="title title-your">Your</span>
      <span class="title title-mentor">Mentor</span>
    </h1>

    <svg class="hero-illustration" viewBox="0 0 420 380" role="img" aria-label="Illustration of a businessman in a red cape, fist raised, standing beside a stepped colourful pyramid">
      <defs>
        <linearGradient id="art-tones" x1="0" y1="1" x2="1" y2="0">
          <stop offset="0" stop-color="var(--art-red)"/>
          <stop offset="0.4" stop-color="var(--art-orange)"/>
          <stop offset="0.7" stop-color="var(--art-teal)"/>
          <stop offset="1" stop-color="var(--art-green)"/>
        </linearGradient>
      </defs>
      <path d="M20 0 H150 V110 L340 110 L420 260 L250 370 L20 270 Z" fill="url(#art-tones)" opacity="0.55"/>
    </svg>

    <p class="subtitle">How to accelerate your growth through reaching out, getting a response from, and leaving an impression on the people you admire most</p>

    <p class="author-name">AUTHOR NAME</p>
  </main>
</body>
</html>
```